Verpackungen für Sekt/Champagner Flaschen
Zielgruppe
Dekoration für Hochzeiten. Tisch Dekoration für Hochzeiten. Zielgruppe alles was mit Hochzeiten zutun hat
Aufgabenstellung
Wir lassen gerade ein Tube/Dose herstellen, die als Umverpackung oder einfach Verpackung für Sekt/Champagne Flaschen dienen soll die dann auf die Tische für Hochzeit´s Deko kommt um die die Tisch Deko aufzubessern, statt einfach nur eine Sekt Flasche stehen zu haben. .Die Tube wird komplett in weiß sein und alles andere an Design soll in einem Gold sein. Mr&Mrs oder Just Married mit Herzen und alles was sonst dazu gehört, da lassen wir freie Hand.
Das Design soll Schlicht sein aber auch Luxuriös.
Durchmesser der Tube wird 8,5 cm haben und 34-35 cm sein.
Die Goldene Schrift und das Muster soll am Ende in einem Relief Lack auf der Tube erscheinen

```html
<!DOCTYPE html>
<html lang="de">
<head>
<meta charset="utf-8">
<title>Just Married – Tubenverpackung</title>
<link rel="stylesheet" href="https://fonts.googleapis.com/css2?family=Dancing+Script:wght@700&display=swap">
<style>
  :root {
    --backdrop: #f0efeb;
    --tube-white: #f5f5f4;
    --peach: #ecd5ca;
    --mauve: #d9cccb;
    --gold-light: #e4c46a;
    --gold: #a8842f;
    --gold-dark: #6a5120;
  }
  * { margin: 0; padding: 0; box-sizing: border-box; }
  html, body {
    width: 900px;
    height: 1200px;
    overflow: hidden;
    background: var(--backdrop);
  }
  .canvas {
    position: relative;
    width: 900px;
    height: 1200px;
    background: var(--backdrop);
  }
  .tube-label {
    position: absolute;
    left: 293px;
    top: 135px;
    width: 315px;
    height: 912px;
    background: var(--tube-white);
    overflow: hidden;
  }
  .tube-rim {
    position: absolute;
    left: 289px;
    width: 323px;
    height: 14px;
    border-radius: 7px;
    background: linear-gradient(var(--gold-light), var(--gold) 55%, var(--gold-dark));
    z-index: 3;
  }
  .tube-rim--top { top: 128px; }
  .tube-rim--bottom { top: 1034px; }
  .tube-label__art {
    position: absolute;
    inset: 0;
    width: 100%;
    height: 100%;
  }
  .wedding-title {
    position: absolute;
    left: 0;
    right: 0;
    top: 345px;
    text-align: center;
    font-family: "Dancing Script", cursive;
    font-weight: 700;
    color: var(--gold);
    text-shadow: 1px 1px 0 var(--gold-dark), -1px -1px 0 var(--gold-light);
    z-index: 2;
  }
  .wedding-title__just {
    display: block;
    font-size: 62px;
    line-height: 66px;
    margin-left: 20px;
  }
  .wedding-title__married {
    display: block;
    font-size: 82px;
    line-height: 80px;
    margin-top: -12px;
  }
</style>
</head>
<body>
<main class="canvas">
  <div class="tube-rim tube-rim--top"></div>

  <section class="tube-label" aria-label="Abwicklung der Sektflaschen-Tube">
    <svg class="tube-label__art" viewBox="0 0 580 1680" xmlns="http://www.w3.org/2000/svg">
      <defs>
        <linearGradient id="glitterTone" x1="0" y1="0" x2="0" y2="1">
          <stop offset="0" stop-color="#d9b44a" stop-opacity="0.08"/>
          <stop offset="0.45" stop-color="#c9a03a" stop-opacity="0.35"/>
          <stop offset="1" stop-color="#b08a30" stop-opacity="0.08"/>
        </linearGradient>
        <linearGradient id="ornamentTone" x1="0" y1="0" x2="1" y2="0">
          <stop offset="0" stop-color="#a8842f" stop-opacity="0"/>
          <stop offset="0.5" stop-color="#a8842f" stop-opacity="0.45"/>
          <stop offset="1" stop-color="#a8842f" stop-opacity="0"/>
        </linearGradient>
      </defs>

      <path class="shape-peach" fill="var(--peach)"
        d="M0,360 C30,300 80,285 140,275 C150,190 215,160 285,160 C355,160 400,205 400,280 L400,980 L0,980 Z"/>

      <path class="shape-mauve" fill="var(--mauve)"
        d="M300,735 L580,745 L580,1230 C480,1255 390,1265 330,1255 C265,1242 240,1185 240,1100 L240,800 Q245,740 300,735 Z"/>

      <g role="img" aria-label="Goldener Glitzerstreifen, diagonal von oben rechts nach unten links">
        <path fill="url(#glitterTone)"
          d="M440,100 C500,180 520,420 470,640 C420,860 300,1000 260,1200 C230,1360 290,1520 300,1640 C240,1480 150,1300 120,1100 C100,900 260,760 330,520 C370,380 390,200 440,100 Z"/>
      </g>

      <g role="img" aria-label="Goldenes Herz mit Schnörkeln unter dem Schriftzug">
        <ellipse cx="290" cy="965" rx="210" ry="55" fill="url(#ornamentTone)"/>
      </g>
    </svg>

    <h1 class="wedding-title">
      <span class="wedding-title__just">Just</span>
      <span class="wedding-title__married">Married</span>
    </h1>
  </section>

  <div class="tube-rim tube-rim--bottom"></div>
</main>
</body>
</html>
```